Doctors clinic requires stationary designed

We require various types of stationary to be design based on the logo (attached). We require the following:
- Letterhead (A4 Portrait)
- Business Card (must include UV spot on rear)
- With compliments slip (DL Landscape)
- Appointments card (Folded A6)

We are a young clinical practice which boasts a modern and sophisticated approach to medicine so we require something which feels fresh and modern. Please include colours represented in the logo (contrasting teal and grey). We are calling for creative minds to put forth their ideas and we will be actively providing feedback on all designs.

thank you

Clinic

```html
<!DOCTYPE html>
<html lang="en">
<head>
<meta charset="utf-8">
<title>Dr Clara Whitfield — Stationery Set</title>
<link href="https://fonts.googleapis.com/css2?family=Open+Sans:wght@400;600;700&display=swap" rel="stylesheet">
<style>
  :root{
    --teal:#2a9a92;
    --teal-dark:#23857e;
    --grey:#c6c6c6;
    --rule:#cfcfcf;
    --ink:#3a3a3a;
    --paper:#ffffff;
    --board:#6b6b6b;
  }
  *{box-sizing:border-box;margin:0;padding:0}
  html,body{width:1200px;height:849px;overflow:hidden}
  body{background:var(--board);font-family:"Open Sans",Arial,sans-serif;color:var(--ink);position:relative}
  .piece{position:absolute;background:var(--paper);box-shadow:4px 6px 10px rgba(0,0,0,.35);overflow:hidden}

  .brand{display:flex;align-items:center;gap:6px}
  .brand-dot{border:1.5px solid var(--teal);border-radius:50%;flex:none}
  .brand-name{color:var(--teal);font-weight:600;line-height:1.1;white-space:nowrap}
  .brand-role{display:block;font-size:.62em}

  .band{position:absolute;background:var(--teal)}
  .flat-pattern{position:absolute;background:var(--teal)}
  .accent-circle{position:absolute;border:5px solid var(--grey);border-radius:50%}

  /* Letterhead */
  .letterhead{left:335px;top:101px;width:316px;height:447px}
  .letterhead .brand{position:absolute;left:28px;top:16px}
  .letterhead .brand-dot{width:28px;height:28px}
  .letterhead .brand-name{font-size:9px}
  .letterhead .head-rule{position:absolute;left:11px;right:11px;top:54px;height:1px;background:var(--rule)}
  .letter-body{position:absolute;left:28px;top:102px;width:260px;font-size:5.4px;line-height:1.5;color:#444}
  .letter-body .salutation{font-size:6.4px;margin-bottom:19px;margin-left:12px}
  .letter-body p{margin-bottom:11px}
  .letter-close{position:absolute;left:38px;top:271px;font-size:6.2px;line-height:1.5}
  .signature{position:absolute;left:38px;top:296px;width:72px;height:34px;background:linear-gradient(90deg,rgba(42,154,146,.25),rgba(42,154,146,.08))}
  .letterhead .accent-circle{width:120px;height:120px;right:-24px;bottom:-26px}
  .letter-foot{position:absolute;left:28px;top:418px;font-size:5.4px;font-weight:700;color:var(--teal);line-height:1.7}
  .letter-foot .sep{margin:0 4px}
  .letter-foot .phone{display:block;padding-left:56px}

  /* Business card back / front */
  .card-top{left:719px;top:156px;width:222px;height:157px}
  .card-top .flat-pattern{left:0;top:0;width:111px;height:157px}
  .card-top .brand{position:absolute;left:123px;top:67px}
  .card-top .brand-dot{width:20px;height:20px}
  .card-top .brand-name{font-size:6.6px}

  /* Appointment card */
  .appt{left:719px;top:345px;width:222px;height:158px}
  .appt .band{left:0;top:0;width:111px;height:158px}
  .appt .center-mark{position:absolute;left:37px;top:61px;width:36px;height:36px;border:1.5px solid rgba(255,255,255,.75);border-radius:50%}
  .appt .brand{position:absolute;left:134px;top:18px}
  .appt .brand-dot{width:17px;height:17px}
  .appt .brand-name{font-size:5.6px}
  .appt-fields{position:absolute;left:127px;top:74px;width:82px;font-size:6px;font-weight:700;color:var(--teal)}
  .appt-fields div{display:flex;align-items:flex-end;gap:4px;height:9px}
  .appt-fields span.line{flex:1;border-bottom:1px dotted #aaa;margin-bottom:2px}
  .appt-note{position:absolute;left:127px;top:128px;width:84px;font-size:3.4px;line-height:1.4;color:var(--teal)}

  /* Small business cards */
  .bc-back{left:257px;top:633px;width:146px;height:102px;box-shadow:3px 5px 8px rgba(0,0,0,.3)}
  .bc-back .flat-pattern{inset:0}
  .bc-front{left:306px;top:677px;width:142px;height:88px}
  .bc-front .brand{position:absolute;left:8px;top:7px}
  .bc-front .brand-dot{width:15px;height:15px}
  .bc-front .brand-name{font-size:5px}
  .bc-front .accent-circle{width:48px;height:48px;right:-8px;bottom:-6px;border-width:3px}
  .bc-contact{position:absolute;left:7px;top:66px;font-size:3.8px;font-weight:700;color:var(--teal);line-height:1.45}

  /* Compliments slip */
  .comp{left:546px;top:615px;width:331px;height:165px}
  .comp .brand{position:absolute;left:13px;top:10px}
  .comp .brand-dot{width:24px;height:24px}
  .comp .brand-name{font-size:8px}
  .comp .accent-circle{width:86px;height:86px;right:-6px;bottom:10px;border-width:4px}
  .comp-foot{position:absolute;left:13px;top:148px;font-size:5.4px;font-weight:700;color:var(--teal);white-space:nowrap}
  .comp-foot .sep{margin:0 4px}
</style>
</head>
<body>

<section class="piece letterhead" aria-label="Letterhead">
  <div class="brand">
    <span class="brand-dot"></span>
    <span class="brand-name">Dr Clara Whitfield<span class="brand-role">Obstetrician &amp; Gynaecologist</span></span>
  </div>
  <div class="head-rule"></div>
  <div class="letter-body">
    <p class="salutation">Dear madam,</p>
    <p>Lorem ipsum dolor sit amet, quam ultrices. Ac nibh. Eget ac, quis mauris vulputate. Felis ultricies. Pharetra habitasse at. Wisi eget nostra. Id fermentum, habitasse nunc ut, morbi et. Vitae elit, nunc in auctor, cras vestibulum. Erat euismod natoque.</p>
    <p>Felis rutrum. Vulputate nam lacus. Luctus morbi. Sapien consectetuer tempor, id nibh. Eu interdum, suscipit ut torquent. Eleifend ornare eleifend, nec malesuada, hendrerit erat pellentesque. Tempore metus est, nullam diam viverra. Nullam sed, erat et.</p>
    <p>Felis velit in, non magnis auctor. Hac fusce tempor. Eleifend lectus non, malesuada etiam at. Pede nisl tortor. Ut ligula morbi, aliquet vestibulum. Aenean tortor eu, nulla vel faucibus. Vestibulum rutrum. Wisi hendrerit sed, maecenas dui augue. Turpis dictumst, pellentesque vestibulum id.</p>
  </div>
  <div class="letter-close">Sincerely yours,<br>Dr. Clara Whitfield</div>
  <div class="signature" role="img" aria-label="Handwritten signature of Dr. Clara Whitfield"></div>
  <div class="accent-circle"></div>
  <div class="letter-foot">Harlow Medical Ctr<span class="sep">|</span>42 Linden Grove Ave, Ashford, PA 17590<span class="phone">Phone: (555) 240-3187</span></div>
</section>

<section class="piece card-top" aria-label="Business card, front and reverse">
  <div class="flat-pattern" role="img" aria-label="Teal panel with repeating spot-UV floral pattern"></div>
  <div class="brand">
    <span class="brand-dot"></span>
    <span class="brand-name">Dr Clara Whitfield<span class="brand-role">Obstetrician &amp; Gynaecologist</span></span>
  </div>
</section>

<section class="piece appt" aria-label="Folded appointment card">
  <div class="band"></div>
  <div class="center-mark"></div>
  <div class="brand">
    <span class="brand-dot"></span>
    <span class="brand-name">Dr Clara Whitfield<span class="brand-role">Obstetrician &amp; Gynaecologist</span></span>
  </div>
  <div class="appt-fields">
    <div>Date <span class="line"></span></div>
    <div>Time <span class="line"></span></div>
  </div>
  <p class="appt-note">Please call at least 24 hours ahead if you need to change your appointment time.</p>
</section>

<section class="piece bc-back" aria-label="Business card reverse">
  <div class="flat-pattern" role="img" aria-label="Teal card with repeating spot-UV floral pattern"></div>
</section>

<section class="piece bc-front" aria-label="Business card front">
  <div class="brand">
    <span class="brand-dot"></span>
    <span class="brand-name">Dr Clara Whitfield<span class="brand-role">Obstetrician &amp; Gynaecologist</span></span>
  </div>
  <div class="accent-circle"></div>
  <div class="bc-contact">Harlow Medical Ctr<br>Phone: (555) 240-3187<br>42 Linden Grove Ave, Ashford, PA 17590</div>
</section>

<section class="piece comp" aria-label="With compliments slip">
  <div class="brand">
    <span class="brand-dot"></span>
    <span class="brand-name">Dr Clara Whitfield<span class="brand-role">Obstetrician &amp; Gynaecologist</span></span>
  </div>
  <div class="accent-circle"></div>
  <div class="comp-foot">Harlow Medical Ctr<span class="sep">|</span>42 Linden Grove Ave, Ashford, PA 17590<span class="sep">|</span>Phone: (555) 240-3187</div>
</section>

</body>
</html>
```